Add words, element to an already make product design

Hi guys,
I m already have the design (attached) which is a wet tissue product. The front main side (about 14cm x 7 cm) is the waves and the brand name Zelfo. However, in this main side, it should contain more words, which are "Khan uot" (mean wet wipe), and the words "Mat lanh" (mean cooling) and "Tinh khiet" (mean purity). "Khan uot" to indicate function of the product, while Mat lanh and Tinh khiet are just marketing term to add.
So yes, the task is quite simple, but I think the key is to choose an appropriate font, color and the location you decide where it should be. You can add any element you want, as long as it look good overall, and those words above, are required to have. More in the attached are few rival from our market, as some example.
Thank you, and wait your idea.

Hi guys, Just to tell you that the main front design will not change. So the waves and the brand name still keep the same. Just adding more words or elements to it. Thank you guys.

```html
<!DOCTYPE html>
<html lang="vi">
<head>
<meta charset="utf-8">
<title>Zelfo – Khan uot packaging layout</title>
<link rel="stylesheet" href="https://fonts.googleapis.com/css2?family=Tinos:wght@400;700&family=Open+Sans:wght@400;600;700&display=swap">
<style>
  :root {
    --ink: #1e1e1e;
    --guide-grey: #b9b9b9;
    --brand-blue: #40c0ec;
    --info-blue: #3aa3df;
    --magenta: #f412d6;
    --white: #ffffff;
    --sea-light: #8fe3ee;
    --sea-mid: #3aaee6;
    --sea-deep: #1a78d8;
  }
  html, body { margin: 0; padding: 0; overflow: hidden; background: var(--white); }
  .dieline-sheet { display: block; width: 1145px; height: 1200px; }

  .cut-line { stroke: var(--ink); stroke-width: 2.4; stroke-dasharray: 18 10; fill: none; }
  .fold-line { stroke: var(--ink); stroke-width: 2.4; fill: none; }
  .ghost-line { stroke: var(--guide-grey); stroke-width: 1.4; stroke-dasharray: 12 6; fill: none; }
  .ghost-dot { stroke: #555; stroke-width: 1.2; stroke-dasharray: 4 4; fill: none; }
  .dimension { font-family: "Open Sans", sans-serif; font-weight: 700; fill: var(--ink); }
  .dimension-ghost { font-family: "Open Sans", sans-serif; font-weight: 400; fill: var(--guide-grey); }

  .serif-copy { font-family: "Tinos", serif; }
  .claim { fill: var(--magenta); }
  .brand-name { font-family: "Tinos", serif; font-weight: 700; fill: var(--brand-blue); }
  .product-tag { fill: var(--white); letter-spacing: 6px; }
  .tag-pill { fill: var(--magenta); }
  .effect-ring { fill: none; stroke: var(--brand-blue); stroke-width: 5; }
  .feature-chip { fill: var(--brand-blue); }
  .material-line { fill: var(--white); }
  .label-window { fill: var(--white); }

  .info-copy { font-family: "Open Sans", sans-serif; fill: var(--info-blue); }
  .usage-pictogram { fill: var(--white); stroke: var(--info-blue); stroke-width: 2; }
  .test-seal { fill: var(--info-blue); stroke: var(--info-blue); }
  .batch-mark { fill: var(--brand-blue); }
  .batch-text { font-family: "Open Sans", sans-serif; font-size: 11px; font-weight: 600; fill: var(--ink); }
</style>
</head>
<body>
<svg class="dieline-sheet" viewBox="0 0 1145 1200" xmlns="http://www.w3.org/2000/svg">
  <defs>
    <linearGradient id="sea-gradient" x1="0" y1="0" x2="0" y2="1">
      <stop offset="0" stop-color="#ffffff"/>
      <stop offset="0.18" stop-color="var(--sea-light)"/>
      <stop offset="0.45" stop-color="#5cc9ec"/>
      <stop offset="0.62" stop-color="var(--sea-mid)"/>
      <stop offset="1" stop-color="var(--sea-deep)"/>
    </linearGradient>
  </defs>

  <!-- secondary guide marks -->
  <g class="secondary-guides">
    <line class="ghost-line" x1="0" y1="98" x2="574" y2="98"/>
    <line class="ghost-line" x1="0" y1="266" x2="574" y2="266"/>
    <line class="ghost-dot" x1="443" y1="104" x2="443" y2="500"/>
    <line class="ghost-dot" x1="525" y1="104" x2="525" y2="500"/>
    <text class="dimension-ghost" x="485" y="64" font-size="40" text-anchor="middle">12.5</text>
    <text class="dimension-ghost" x="0" y="64" font-size="40">12.5</text>
  </g>

  <!-- front panel artwork -->
  <g class="front-panel">
    <rect x="123" y="540" width="892" height="518" fill="url(#sea-gradient)" role="img" aria-label="Soft watercolour waves in cyan and ocean blue"/>
    <rect class="label-window" x="724" y="871" width="253" height="100"/>

    <text class="serif-copy claim" x="160" y="464" font-size="24">Dernatologically Tested</text>

    <circle class="effect-ring" cx="258" cy="541" r="61"/>
    <text class="serif-copy claim" x="258" y="552" font-size="48" text-anchor="middle">99%</text>
    <text class="serif-copy claim" x="258" y="570" font-size="17" text-anchor="middle">EFFECTIVE</text>

    <text class="serif-copy claim" x="408" y="545" font-size="26">Clean and Germ Free Feeling</text>

    <text class="brand-name" x="574" y="655" font-size="150" text-anchor="middle">Zelfo</text>

    <rect class="tag-pill" x="442" y="670" width="269" height="50" rx="25"/>
    <text class="serif-copy product-tag" x="576" y="712" font-size="46" text-anchor="middle">Khan uot</text>

    <rect class="feature-chip" x="754" y="455" width="47" height="47" rx="8" role="img" aria-label="Purity icon"/>
    <rect class="feature-chip" x="757" y="508" width="47" height="47" rx="8" role="img" aria-label="Cooling leaf icon"/>
    <text class="serif-copy claim" x="818" y="490" font-size="43">Tinh khie</text>
    <text class="serif-copy claim" x="824" y="543" font-size="43">Mat lanh</text>

    <text class="serif-copy material-line" x="172" y="790" font-size="34" textLength="805" lengthAdjust="spacingAndGlyphs">Wipes made from 100% Natural and Biodegradable Materials</text>
  </g>

  <!-- top flap info -->
  <g class="top-flap">
    <text class="info-copy" x="420" y="203" font-size="12.5">NSX: 2 năm trước HSD</text>
    <text class="info-copy" x="420" y="217" font-size="12.5">HSD: In trên bao bì</text>

    <g transform="rotate(180 247 243)">
      <text class="info-copy" x="247" y="240" font-size="9.5" text-anchor="middle">XIN BỎ VÀO ĐÚNG</text>
      <text class="info-copy" x="247" y="253" font-size="9.5" text-anchor="middle">NƠI QUY ĐỊNH</text>
    </g>

    <g class="usage-pictograms" role="img" aria-label="Usage pictograms for wiping hands, face, travel and baby care">
      <rect class="usage-pictogram" x="300" y="224" width="37" height="37" rx="5"/>
      <rect class="usage-pictogram" x="347" y="224" width="37" height="37" rx="5"/>
      <rect class="usage-pictogram" x="394" y="224" width="37" height="37" rx="5"/>
      <rect class="usage-pictogram" x="300" y="270" width="37" height="37" rx="5"/>
      <rect class="usage-pictogram" x="347" y="270" width="37" height="37" rx="5"/>
      <rect class="usage-pictogram" x="394" y="270" width="37" height="37" rx="5"/>
      <rect class="usage-pictogram" x="229" y="264" width="36" height="36" rx="5"/>
    </g>

    <path class="test-seal" d="M895 200 L957 227 L950 300 L895 311 L840 300 L833 227 Z" role="img" aria-label="Laboratory test seal"/>
  </g>

  <!-- dieline -->
  <g class="dieline">
    <rect class="cut-line" x="41" y="50" width="1058" height="1089"/>
    <line class="cut-line" x1="123" y1="50" x2="123" y2="1139"/>
    <line class="cut-line" x1="1015" y1="50" x2="1015" y2="1139"/>
    <line class="cut-line" x1="41" y1="131" x2="1099" y2="131"/>
    <line class="cut-line" x1="41" y1="364" x2="1099" y2="364"/>
    <line class="cut-line" x1="41" y1="826" x2="1099" y2="826"/>
    <line class="cut-line" x1="41" y1="1058" x2="1099" y2="1058"/>
    <line class="fold-line" x1="123" y1="826" x2="1015" y2="826"/>
    <line class="fold-line" x1="123" y1="1058" x2="1015" y2="1058"/>
    <line class="fold-line" x1="123" y1="826" x2="123" y2="1058"/>
  </g>

  <rect class="batch-mark" x="41" y="1074" width="32" height="65"/>
  <text class="batch-text" transform="translate(45 1079) rotate(90)">BH</text>

  <!-- dimensions -->
  <g class="dimensions">
    <text class="dimension" x="92" y="32" font-size="36" text-anchor="middle">12.5</text>
    <text class="dimension" x="570" y="32" font-size="42" text-anchor="middle">135</text>
    <text class="dimension" x="1058" y="32" font-size="36" text-anchor="middle">12.5</text>
    <text class="dimension" x="565" y="1198" font-size="42" text-anchor="middle">160 mm</text>
    <text class="dimension" transform="translate(30 598) rotate(-90)" font-size="40" text-anchor="middle">165mm</text>
    <g font-size="26">
      <text class="dimension" transform="translate(1124 76) rotate(90)" text-anchor="middle">12.5</text>
      <text class="dimension" transform="translate(1124 217) rotate(90)" text-anchor="middle">35</text>
      <text class="dimension" transform="translate(1124 562) rotate(90)" text-anchor="middle">70</text>
      <text class="dimension" transform="translate(1124 913) rotate(90)" text-anchor="middle">35</text>
      <text class="dimension" transform="translate(1124 1102) rotate(90)" text-anchor="middle">12.5</text>
    </g>
  </g>
</svg>
</body>
</html>
```